TK Alarm 'Welcome' Envelope

I am looking for a 'Welcome' envelope design for new customers who sign up for our Alarm Services. In this envelope we will send confidential documents that the customer will need. I want it to stand out, yet look classy.

```html
<!DOCTYPE html>
<html lang="en">
<head>
<meta charset="utf-8">
<title>TK Alarm Welcome Envelope</title>
<link href="https://fonts.googleapis.com/css2?family=Poppins:wght@300;400;600;700;800&display=swap" rel="stylesheet">
<style>
  :root{
    --page:#ffffff;
    --label:#6b6f72;
    --env-dark:#07141c;
    --env-mid:#0b3146;
    --env-glow:#0f4a63;
    --band:#0d3b50;
    --flap:#0a3040;
    --brand-green:#5cc431;
    --text-light:#ffffff;
    --title:#cdd5d9;
    --ghost:rgba(255,255,255,0.07);
    --ghost-text:rgba(255,255,255,0.16);
    --icon:#b9c3c8;
    --icon-blue:#2f8fd6;
  }
  *{margin:0;padding:0;box-sizing:border-box}
  html,body{width:806px;height:1200px;overflow:hidden;background:var(--page)}
  body{position:relative;font-family:'Poppins',sans-serif}

  .sheet-label{position:absolute;font-weight:300;font-size:21px;color:var(--label);letter-spacing:0.5px}

  .envelope{position:absolute;width:688px;height:296px;overflow:hidden;background:var(--env-dark)}
  .envelope-art{position:absolute;inset:0;
    background:
      radial-gradient(circle at 350px 150px, #2a7fc4 0 22px, #0f5a80 23px 40px, transparent 41px),
      radial-gradient(circle at 350px 150px, var(--env-glow) 0, var(--env-mid) 150px, transparent 300px),
      linear-gradient(90deg, var(--env-dark) 0%, #0a2534 45%, #0a2534 70%, var(--env-dark) 100%);}
  .lens-band{position:absolute;left:0;right:0;height:28px;background:var(--band);opacity:0.85}

  .ghost-panel{position:absolute;left:458px;top:64px;width:226px;height:134px;background:var(--ghost);
    clip-path:polygon(18% 0,82% 0,100% 45%,82% 100%,18% 100%,0 45%)}
  .ghost-name{position:absolute;left:468px;top:108px;width:206px;text-align:center;font-weight:700;font-size:30px;color:var(--ghost-text)}
  .ghost-tag{position:absolute;left:458px;width:226px;text-align:center;font-size:6px;color:var(--ghost-text)}
  .ghost-line{position:absolute;left:458px;width:226px;text-align:center;font-size:7px;color:var(--ghost-text);line-height:11px}

  .brand-name{position:absolute;font-weight:700;font-size:30px;line-height:1;color:var(--brand-green);letter-spacing:1px}

  .return-address{position:absolute;left:48px;color:var(--text-light)}
  .contact-row{position:absolute;display:flex;align-items:center;gap:8px;color:var(--text-light)}
  .contact-row svg,.return-address svg{flex:none}
  .pin{position:absolute;left:-22px;top:3px}

  .font-one .return-address{top:76px;font-weight:700;font-size:11px;line-height:13px}
  .font-one .phone{top:147px;left:31px;font-weight:800;font-size:16px}
  .font-one .hours{top:171px;left:31px;font-weight:700;font-size:11px}

  .font-two .return-address{top:74px;left:44px;font-weight:400;font-size:12px;line-height:19px}
  .font-two .phone{top:148px;left:24px;font-weight:400;font-size:13px}
  .font-two .hours{top:170px;left:24px;font-weight:400;font-size:12px}

  .address-window{position:absolute;left:23px;top:200px;width:211px;height:73px;background:#fff;border-radius:8px}
  .doc-title{position:absolute;right:13px;top:224px;font-weight:300;font-size:27px;color:var(--title);letter-spacing:0.5px}

  .back-flap{position:absolute;left:0;top:0;width:688px;height:46px;background:var(--flap);
    clip-path:polygon(0 0,100% 0,95% 100%,5% 100%)}
  .back-brand{left:0;right:0;top:210px;text-align:center;font-size:24px}
  .back-tagline{position:absolute;left:0;right:0;top:252px;text-align:center;font-size:13px;color:var(--text-light)}
</style>
</head>
<body>

<p class="sheet-label" style="left:42px;top:24px">FRONT 1 (FONT #1)</p>
<section class="envelope font-one" style="left:57px;top:92px">
  <div class="envelope-art" role="img" aria-label="Dark teal camera lens and shutter illustration"></div>
  <div class="lens-band" style="top:227px"></div>
  <div class="ghost-panel"></div>
  <p class="ghost-tag" style="top:50px">Security Products Dealer</p>
  <p class="ghost-name">TK Alarm</p>
  <p class="ghost-line" style="top:200px">24 Hour Protection<br>888-555-0142</p>

  <p class="brand-name" style="left:23px;top:38px">TK Alarm</p>
  <address class="return-address" style="font-style:normal">
    <svg class="pin" width="12" height="18" viewBox="0 0 12 18"><path d="M6 0a6 6 0 0 0-6 6c0 4.5 6 12 6 12s6-7.5 6-12a6 6 0 0 0-6-6z" fill="var(--icon)"/><circle cx="6" cy="6" r="2.3" fill="var(--env-dark)"/></svg>
    PO Box 40215<br>Fairview, ID 83700
  </address>
  <p class="contact-row phone">
    <svg width="14" height="14" viewBox="0 0 14 14"><rect width="14" height="14" rx="3" fill="var(--icon)"/><path d="M4 3.5l1.6 0 .6 2-1 .8a6 6 0 0 0 2.5 2.5l.8-1 2 .6 0 1.6a1 1 0 0 1-1 1A7 7 0 0 1 3 4.5a1 1 0 0 1 1-1z" fill="var(--env-dark)"/></svg>
    888 - 555 - 0142
  </p>
  <p class="contact-row hours">
    <svg width="16" height="16" viewBox="0 0 16 16"><path d="M3 4a6 6 0 1 1-1 4" fill="none" stroke="var(--icon)" stroke-width="2"/><path d="M1 2l2 2.5 2.5-1.5" fill="none" stroke="var(--icon)" stroke-width="1.6"/><path d="M8 5v3.5h2.5" fill="none" stroke="var(--icon)" stroke-width="1.6"/></svg>
    24 HOUR PROTECTION
  </p>
  <div class="address-window"></div>
  <h2 class="doc-title">WELCOME LETTER</h2>
</section>

<p class="sheet-label" style="left:48px;top:446px">FRONT 2 (FONT #2)</p>
<section class="envelope font-two" style="left:49px;top:488px">
  <div class="envelope-art" role="img" aria-label="Dark teal camera lens and shutter illustration"></div>
  <div class="lens-band" style="top:227px"></div>
  <div class="ghost-panel"></div>
  <p class="ghost-tag" style="top:50px">Security Products Dealer</p>
  <p class="ghost-name">TK Alarm</p>
  <p class="ghost-line" style="top:200px">24 Hour Protection<br>888-555-0142</p>

  <p class="brand-name" style="left:24px;top:38px">TK Alarm</p>
  <address class="return-address" style="font-style:normal">
    <svg class="pin" width="12" height="18" viewBox="0 0 12 18"><path d="M6 0a6 6 0 0 0-6 6c0 4.5 6 12 6 12s6-7.5 6-12a6 6 0 0 0-6-6z" fill="var(--icon-blue)"/><circle cx="6" cy="6" r="2.3" fill="var(--env-dark)"/></svg>
    PO Box 40215<br>Fairview, ID 83700
  </address>
  <p class="contact-row phone">
    <svg width="14" height="14" viewBox="0 0 14 14"><rect width="14" height="14" rx="3" fill="var(--icon-blue)"/><path d="M4 3.5l1.6 0 .6 2-1 .8a6 6 0 0 0 2.5 2.5l.8-1 2 .6 0 1.6a1 1 0 0 1-1 1A7 7 0 0 1 3 4.5a1 1 0 0 1 1-1z" fill="var(--env-dark)"/></svg>
    888 . 555 . 0142
  </p>
  <p class="contact-row hours">
    <svg width="16" height="16" viewBox="0 0 16 16"><path d="M3 4a6 6 0 1 1-1 4" fill="none" stroke="var(--icon-blue)" stroke-width="2"/><path d="M1 2l2 2.5 2.5-1.5" fill="none" stroke="var(--icon-blue)" stroke-width="1.6"/><path d="M8 5v3.5h2.5" fill="none" stroke="var(--icon-blue)" stroke-width="1.6"/></svg>
    24 HOUR PROTECTION
  </p>
  <div class="address-window"></div>
  <h2 class="doc-title">WELCOME LETTER</h2>
</section>

<p class="sheet-label" style="left:56px;top:822px">BACK</p>
<section class="envelope envelope-back" style="left:57px;top:861px">
  <div class="envelope-art" role="img" aria-label="Dark teal camera lens and shutter illustration"></div>
  <div class="back-flap"></div>
  <div class="lens-band" style="top:220px"></div>
  <div class="ghost-panel" style="top:84px"></div>
  <p class="ghost-tag" style="top:66px">Security Products Dealer</p>
  <p class="ghost-name" style="top:128px">TK Alarm</p>
  <p class="ghost-line" style="top:220px">24 Hour Protection<br>888-555-0142</p>

  <p class="brand-name back-brand">TK Alarm</p>
  <p class="back-tagline">SECURITY PRODUCTS DEALER</p>
</section>

</body>
</html>
```